Web Design (Coded) and Project - Finance Company

Tallowen Lending Group is a mortgage broker company based in Sydney Australia and provides lending solutions for individuals and businesses.

Our target market is anyone with the financial means to get a loan.

I am looking for a website design in this contest. The site needs to be able to be viewed on a portable device such as Veltab, Velfon, etc.

I have the logo design and files which need to be used. I also have the BLQR logo which will need to be in the footer of each page.

The website needs to represent a big finance company with integrity and knowledge.

The website will need to be uploaded to Pelwickhost.com.au as they are the hosting provider. I will also need the ability to make changes to the text and pictures in the future and upload the revisions. I need the website ready to go and ready to be uploaded onto Pelwick Host.

The website will consist of 6 pages in total There are 4 main pages that will be viewed and then 2 with Privacy and Internal Dispute Resolution which are only accessed through links. These will be as follows:

Home
I would prefer to have a fresh bright and professional looking home page given that most mortgage broker websites look the same with the menu buttons at the top.

Services
Details the loan types that we handle and some text for each one.

About Us
I have the text for this.

Contact Us
Form to have the following inputs:
• Surname
• First Name
• Suburb
• State
• Phone number
• Mobile number
• Email address
• Preferred contact
o Phone
o Mobile
o Email
• Reason for Enquiry
o First home buyer
o Refinance
o Investment Property
o Commercial lending
o Personal loan
o Other
• Comments

Privacy
This page will only be accessed from a link at the bottom of each page. I have the wording that I will provide.

Dispute Resolution Policy
This page will only be accessed from a link on the Contact Us page. I have the wording that I will provide.
Updates

The designs that are coming through so far are generally looking the same generic website layout. I am looking for the home page to be something different with more of a wow factor and something different to the standard page link menu accross the top of the screen. The content should be fairly minimal given that I am a new business there will be limited text for each page. I am happy to increase the budget if required as I appreciate there will be more work involved.

Reason: I am extending the deadline as the design so far are good but fairly generic and template style home pages. For the home page I am looking for something a little more striking with a visual impact.

I have increased the payment by $200 to encourage more designs. Designs need to be relevant to the business, the number of pages and content. Several designs have come through looking good but just look like a standard template with my logo added, but the content does not match the business.

The brief stated that I am looking for the home page to be something different with more of a wow factor and something different to the standard page link menu accross the top of the screen. All of the designs have come through with the navigation bar along the top and a generic layout. I have attached a couple of idea's. Obviously these do not relate to the finance and mortgage industry but you can see the sort of style that gives the site a wow factor. The other pages can be more generic, but the first page is the attention grabber. You can also see the VelFon view that I am after. These are just templates from Pelwick Host that I could use to build the site, I just don't have the time or creative flair. Please submit more designs. Thanks for your work to date, Rob.

Hi. Could you please submit designs based on brief and the two screen shots attached. Mobile device view should work as per screen shots. Thanks, Rob

Reason: Still looking for designs to meet the brief provided.

Industry/Entity Type

Financial

Requirements
Must have
• Colour palette to be as supplied. I will post this shortly.
Should not have
• No cheesy smiley faces
No handshaking
No money pictures
No pictures of stones
No picture of people in an office looking at things
No lime green or purple in colour
Would prefer not to have a picture of the Corvell Arch or Marlow Hall

```html
<!DOCTYPE html>
<html lang="en">
<head>
<meta charset="utf-8">
<title>Tallowen Lending Group</title>
<link rel="stylesheet" href="https://fonts.googleapis.com/css2?family=Open+Sans:wght@400;600;700&family=Rokkitt:wght@400&family=Arimo:wght@400&display=swap">
<style>
:root{
  --blue:#0aa6e3;
  --navy:#0b5d82;
  --ink:#3d3d3f;
  --text:#333333;
  --muted:#7a7a7a;
  --bg:#ececec;
  --band:#3f3f41;
  --white:#ffffff;
  --line:#b9b9b9;
}
*{box-sizing:border-box;margin:0;padding:0}
html,body{width:1200px;height:1054px;overflow:hidden}
body{position:relative;background:var(--bg);font-family:"Arimo",Arial,sans-serif;color:var(--text)}
.abs{position:absolute}
.hero-art{left:0;top:49px;width:1200px;height:797px;
  background:radial-gradient(ellipse 520px 360px at 620px 300px,#fbfbfb 0%,rgba(251,251,251,0) 70%),
  linear-gradient(160deg,#dcdcdc 0%,#f2f2f2 35%,#e4e4e4 70%,#e9e9e9 100%)}
.topbar{left:0;top:0;width:1200px;height:49px;background:#f4f4f4;border-bottom:1px solid #dedede}
.welcome{left:0;width:1200px;top:16px;text-align:center;font-family:"Rokkitt",serif;font-size:19px;color:var(--ink)}
.toplinks{left:858px;top:19px;font-size:11px;color:var(--muted);letter-spacing:.2px}
.toplinks a{color:var(--muted);text-decoration:none}
.pointer{left:558px;top:46px}
.brand{left:472px;top:112px;width:300px;height:94px}
.brand-divider{left:584px;top:84px;width:1px;height:140px;background:linear-gradient(#f4f4f4,#bdbdbd,#f4f4f4)}
.brand-dot{left:476px;top:126px;width:64px;height:64px;border-radius:50%;background:var(--navy)}
.brand-name{left:600px;top:104px;font-family:"Open Sans",sans-serif;font-weight:700;font-size:31px;line-height:33px;color:var(--ink);letter-spacing:-.3px}
.nav{left:326px;top:242px;height:59px;display:flex;font-family:"Rokkitt",serif;font-size:21px;color:var(--ink)}
.nav a{color:var(--ink);text-decoration:none;display:flex;align-items:center;padding:0 21px;height:59px;border-left:1px solid #d6d6d6}
.nav a.active{background:var(--blue);color:var(--white);border-left:0;padding:0 25px}
.nav a.active+a{border-left:0}
.nav-rule{left:162px;top:300px;width:877px;border-top:1px dotted #a9a9a9}
.headline-1{left:209px;top:342px;font-family:"Open Sans",sans-serif;font-size:47px;color:var(--ink);letter-spacing:-3.2px;font-weight:400}
.headline-2{left:206px;top:384px;font-family:"Open Sans",sans-serif;font-weight:700;font-size:72px;letter-spacing:-6px;line-height:90px;white-space:nowrap}
.headline-2 .b1{color:var(--blue)}
.headline-2 .amp{color:var(--ink)}
.headline-2 .b2{color:var(--navy)}
.intro{left:300px;top:466px;width:720px;text-align:center;font-family:"Open Sans",sans-serif;font-size:16px;line-height:27px;color:#1d1d1d}
.readmore-frame{left:470px;top:529px;width:267px;height:77px;border-radius:9px;background:#f6f6f6;box-shadow:0 2px 6px rgba(0,0,0,.18)}
.readmore{left:476px;top:537px;width:255px;height:61px;border-radius:7px;background:var(--band);color:var(--white);font-family:"Rokkitt",serif;font-size:34px;display:flex;align-items:center;justify-content:center;padding-left:30px;letter-spacing:-.6px}
.hero-shadow{left:162px;top:628px;width:877px;height:12px;background:radial-gradient(ellipse 50% 100% at 50% 0%,rgba(0,0,0,.45),rgba(0,0,0,0) 70%)}
.about-title{left:162px;top:684px;font-family:"Open Sans",sans-serif;font-size:35px;letter-spacing:-2.8px;color:var(--ink)}
.about-tag{left:163px;top:735px;font-family:"Open Sans",sans-serif;font-weight:600;font-size:11px;color:var(--navy);letter-spacing:-.3px}
.about-copy{left:163px;top:758px;width:530px;font-size:11px;line-height:16px;color:var(--text)}
.more{left:162px;top:796px;width:67px;height:29px;background:var(--band);color:var(--white);font-family:"Rokkitt",serif;font-size:17px;display:flex;align-items:center;justify-content:center}
.col-divider{left:712px;top:692px;height:136px;border-left:1px dotted #9a9a9a}
.finance-title{left:752px;top:690px;font-family:"Open Sans",sans-serif;font-size:25px;letter-spacing:-1.8px;color:var(--navy)}
.finance-list{left:753px;top:747px;width:290px;display:grid;grid-template-columns:136px 154px;row-gap:8px;font-size:11px;color:#444;list-style:none}
.finance-list li{display:flex;align-items:center;gap:8px;height:14px}
.finance-list svg{flex:none}
.newsletter{left:0;top:846px;width:1200px;height:106px;background:var(--band)}
.news-title{left:184px;top:860px;font-family:"Rokkitt",serif;font-size:26px;color:var(--white);letter-spacing:-.8px}
.field{top:901px;width:355px;height:31px;background:var(--white);border:1px solid #9d9d9d}
.subscribe{left:909px;top:901px;width:110px;height:31px;background:var(--blue);color:var(--white);font-family:"Rokkitt",serif;font-size:18px;display:flex;align-items:center;justify-content:center}
.social{left:163px;top:971px;display:flex;gap:10px}
.social span{width:14px;height:14px;border-radius:50%;background:var(--blue);display:block}
.footer-links{left:163px;top:999px;font-size:11px;color:var(--text)}
.copyright{left:163px;top:1020px;font-size:11px;color:var(--text)}
.copyright u{text-decoration:underline}
.badge{left:623px;top:966px;width:188px;height:70px;border:3px solid var(--navy);border-radius:3px;background:linear-gradient(#ffffff,#e6f4fb)}
.footer-dot{left:842px;top:985px;width:40px;height:40px;border-radius:50%;background:var(--navy)}
.footer-brand{left:892px;top:968px;font-family:"Open Sans",sans-serif;font-weight:700;font-size:20px;line-height:22px;color:var(--ink)}
</style>
</head>
<body>
  <div class="abs hero-art" role="img" aria-label="Soft greyscale photo of a hand signing a loan document with a pen, a house faintly behind"></div>

  <header>
    <div class="abs topbar"></div>
    <div class="abs welcome">Welcome To TALLOWEN LENDING GROUP</div>
    <div class="abs toplinks"><a href="#">Privacy</a>&nbsp;-&nbsp; <a href="#">Dispute Resolution Policy</a></div>
    <svg class="abs pointer" width="84" height="35" viewBox="0 0 84 35"><polygon points="0,0 84,0 42,35" fill="var(--blue)"/></svg>

    <div class="abs brand-dot"></div>
    <div class="abs brand-divider"></div>
    <div class="abs brand-name">TALLOWEN<br>LENDING<br>GROUP</div>

    <nav class="abs nav">
      <a class="active" href="#">HOME</a>
      <a href="#">SERVICES</a>
      <a href="#">ABOUT US</a>
      <a href="#">CONTACT US</a>
    </nav>
    <div class="abs nav-rule"></div>
  </header>

  <section>
    <h1 class="abs headline-1">Provides Lending Solutions For</h1>
    <div class="abs headline-2"><span class="b1">INDIVIDUALS</span> <span class="amp">&amp;</span> <span class="b2">BUSINESSES</span></div>
    <p class="abs intro">Tallowen Lending Group is a mortgage broker company based in Sydney Australia and provides lending solutions for individuals and businesses.</p>
    <div class="abs readmore-frame"></div>
    <a class="abs readmore" href="#">Read More...</a>
    <div class="abs hero-shadow"></div>
  </section>

  <section>
    <h2 class="abs about-title">TALLOWEN LENDING GROUP</h2>
    <div class="abs about-tag">GREAT MORTGAGES MADE SIMPLE ( IF YOU KNOW WHERE TO LOOK )</div>
    <p class="abs about-copy">Tallowen Lending Group is a mortgage broker company based in Sydney Australia and provides lending solutions for individuals and businesses. Our target market is anyone with the financial means to get a loan.</p>
    <a class="abs more" href="#">MORE</a>
    <div class="abs col-divider"></div>

    <h2 class="abs finance-title">MORTGAGE FINANCE</h2>
    <ul class="abs finance-list">
      <li><svg width="13" height="13" viewBox="0 0 13 13"><circle cx="6.5" cy="6.5" r="6.5" fill="#8c8c8c"/><path d="M3.5 6.5h5M6.5 4l2.5 2.5-2.5 2.5" stroke="#fff" stroke-width="1.5" fill="none"/></svg>Family Home</li>
      <li><svg width="13" height="13" viewBox="0 0 13 13"><circle cx="6.5" cy="6.5" r="6.5" fill="#8c8c8c"/><path d="M3.5 6.5h5M6.5 4l2.5 2.5-2.5 2.5" stroke="#fff" stroke-width="1.5" fill="none"/></svg>Refinancing</li>
      <li><svg width="13" height="13" viewBox="0 0 13 13"><circle cx="6.5" cy="6.5" r="6.5" fill="#8c8c8c"/><path d="M3.5 6.5h5M6.5 4l2.5 2.5-2.5 2.5" stroke="#fff" stroke-width="1.5" fill="none"/></svg>Investment Property</li>
      <li><svg width="13" height="13" viewBox="0 0 13 13"><circle cx="6.5" cy="6.5" r="6.5" fill="#8c8c8c"/><path d="M3.5 6.5h5M6.5 4l2.5 2.5-2.5 2.5" stroke="#fff" stroke-width="1.5" fill="none"/></svg>Reverse Mortgages</li>
      <li><svg width="13" height="13" viewBox="0 0 13 13"><circle cx="6.5" cy="6.5" r="6.5" fill="#8c8c8c"/><path d="M3.5 6.5h5M6.5 4l2.5 2.5-2.5 2.5" stroke="#fff" stroke-width="1.5" fill="none"/></svg>Commercial Property</li>
      <li><svg width="13" height="13" viewBox="0 0 13 13"><circle cx="6.5" cy="6.5" r="6.5" fill="#8c8c8c"/><path d="M3.5 6.5h5M6.5 4l2.5 2.5-2.5 2.5" stroke="#fff" stroke-width="1.5" fill="none"/></svg>Self Managed Super Fund</li>
      <li><svg width="13" height="13" viewBox="0 0 13 13"><circle cx="6.5" cy="6.5" r="6.5" fill="#8c8c8c"/><path d="M3.5 6.5h5M6.5 4l2.5 2.5-2.5 2.5" stroke="#fff" stroke-width="1.5" fill="none"/></svg>Equity Release</li>
      <li><svg width="13" height="13" viewBox="0 0 13 13"><circle cx="6.5" cy="6.5" r="6.5" fill="#8c8c8c"/><path d="M3.5 6.5h5M6.5 4l2.5 2.5-2.5 2.5" stroke="#fff" stroke-width="1.5" fill="none"/></svg>Property Insurance</li>
    </ul>
  </section>

  <section>
    <div class="abs newsletter"></div>
    <div class="abs news-title">To get FREE Promotion, Please Subscribe To Newsletter</div>
    <div class="abs field" style="left:184px"></div>
    <div class="abs field" style="left:546px"></div>
    <div class="abs subscribe">SUBSCRIBE</div>
  </section>

  <footer>
    <div class="abs social"><span></span><span></span><span></span><span></span><span></span></div>
    <div class="abs footer-links">Home &nbsp;-&nbsp; Services &nbsp;-&nbsp; About Us &nbsp;-&nbsp; Contact Us</div>
    <div class="abs copyright">Copyright © 2012 Tallowen Lending Group. All rights reserved! &nbsp;<u>Legal Information</u> &nbsp;| &nbsp;<u>Faq</u></div>
    <div class="abs badge" role="img" aria-label="Approved broker accreditation badge"></div>
    <div class="abs footer-dot"></div>
    <div class="abs footer-brand">TALLOWEN<br>LENDING<br>GROUP</div>
  </footer>
</body>
</html>
```